Lanterns Over Saltmere - Islamic Book about death, grave and the hereafter

We need a complete redesign of an old book cover. It is a book about death, the grave, the day of judgment, hellfire and paradise. i've attached our old bookcover. you can take new colors and change completly the design. It is up to you!

```html
<!DOCTYPE html>
<html lang="de">
<head>
<meta charset="utf-8">
<title>Lanterns Over Saltmere – Cover</title>
<link href="https://fonts.googleapis.com/css2?family=Tinos:wght@400;700&display=swap" rel="stylesheet">
<style>
  :root {
    --stage: #000000;
    --gold-light: #fff1a8;
    --gold-mid: #e2b53a;
    --gold-deep: #8a5a0c;
    --band-gold: #f1c21c;
    --band-dark: #7a4a06;
    --ink-dark: #2a1a04;
    --sky-top: #6f9fd6;
    --sky-pale: #dbe8f5;
    --haze: #eef3f6;
    --rock: #8b9a9a;
    --meadow: #4f8a34;
    --meadow-deep: #2f5a22;
    --bloom: #f2d21c;
  }
  * { box-sizing: border-box; margin: 0; padding: 0; }
  html, body {
    width: 1200px; height: 818px; overflow: hidden;
    background: var(--stage);
    font-family: "Tinos", "Times New Roman", serif;
  }
  .spread {
    position: absolute; left: 80px; top: 50px;
    width: 1050px; height: 715px;
  }
  .back-cover {
    position: absolute; left: 0; top: 0; width: 486px; height: 715px;
    background:
      radial-gradient(ellipse 60% 30% at 40% 18%, rgba(255,255,255,.55), transparent 70%),
      linear-gradient(180deg, var(--sky-top) 0%, #a9c4e2 22%, var(--sky-pale) 38%, #b9c4c4 52%, var(--rock) 66%, #b8cfa8 80%, var(--meadow) 92%, var(--bloom) 100%);
    filter: saturate(.85);
  }
  .back-cover::after {
    content: ""; position: absolute; inset: 0;
    background: linear-gradient(180deg, transparent 60%, rgba(238,243,246,.45) 80%, transparent 100%);
  }
  .spine {
    position: absolute; left: 486px; top: 0; width: 80px; height: 715px;
    background: linear-gradient(90deg, #c99a2a 0%, #f3d27a 18%, #e6b94a 50%, #b9861e 85%, #8a5a0c 100%);
  }
  .spine-title {
    position: absolute; left: 40px; top: 302px;
    transform: translate(-50%, -50%) rotate(-90deg);
    white-space: nowrap;
    font-size: 32px; color: var(--band-dark);
    letter-spacing: .5px;
  }
  .spine-title .caps { text-transform: uppercase; }
  .spine-imprint {
    position: absolute; left: 14px; top: 590px; width: 52px; height: 84px;
    background: #e9bf56;
    display: flex; flex-direction: column; align-items: center; justify-content: center; gap: 6px;
  }
  .spine-imprint .mark { width: 18px; height: 18px; background: var(--band-dark); }
  .spine-imprint .name {
    font-size: 7px; color: var(--ink-dark); text-align: center; line-height: 1.1;
  }
  .front-cover {
    position: absolute; left: 566px; top: 0; width: 484px; height: 715px; overflow: hidden;
  }
  .front-scene {
    position: absolute; inset: 0;
    background:
      radial-gradient(ellipse 45% 22% at 55% 45%, rgba(255,255,255,.9), transparent 70%),
      radial-gradient(ellipse 70% 25% at 60% 22%, rgba(255,255,255,.75), transparent 70%),
      linear-gradient(180deg, #a9c6e6 0%, var(--sky-pale) 30%, #ffffff 46%, #7fa0c8 56%, #5d7fb0 62%, var(--meadow) 74%, var(--meadow-deep) 86%, #6f8a2a 94%, var(--bloom) 100%);
  }
  .author {
    position: absolute; left: 0; right: 0; top: 96px; text-align: center;
    font-size: 22px; font-weight: 700; letter-spacing: .5px;
    color: #b98a18;
    text-shadow: 0 1px 1px rgba(60,30,0,.5);
  }
  .gold {
    background: linear-gradient(180deg, var(--gold-light) 0%, var(--gold-mid) 45%, var(--gold-deep) 100%);
    -webkit-background-clip: text; background-clip: text; color: transparent;
    filter: drop-shadow(0 2px 2px rgba(40,20,0,.55));
  }
  .title-lead {
    position: absolute; left: 0; right: 0; top: 260px; text-align: center;
    font-size: 50px; line-height: 1;
  }
  .title-main {
    position: absolute; left: 0; right: 0; top: 318px; text-align: center;
    font-size: 86px; line-height: 1; letter-spacing: 1px; text-transform: uppercase;
  }
  .subtitle-band {
    position: absolute; left: 0; top: 416px; width: 484px; height: 34px;
    background: linear-gradient(90deg, var(--band-dark) 0%, #c28a12 35%, var(--band-gold) 70%, var(--band-gold) 100%);
    display: flex; align-items: center; justify-content: center;
  }
  .subtitle {
    font-size: 27px; color: #fff6dc; text-shadow: 0 1px 2px rgba(0,0,0,.6);
    white-space: nowrap;
  }
  .publisher {
    position: absolute; left: 0; right: 0; top: 705px; transform: translateY(-50%);
    top: 716px; text-align: center;
    font-size: 17px; font-weight: 700; color: #ffe88a;
    text-shadow: 0 1px 2px rgba(40,20,0,.7);
  }
  .publisher { top: 666px; transform: none; }
</style>
</head>
<body>
  <main class="spread">
    <section class="back-cover" role="img" aria-label="Misty mountain peak under a pale blue cloudy sky, fading into a meadow of yellow wildflowers"></section>

    <section class="spine">
      <h2 class="spine-title">Lanterns Over <span class="caps">Saltmere</span></h2>
      <div class="spine-imprint">
        <span class="mark"></span>
        <span class="name">Cedarhall Press</span>
      </div>
    </section>

    <section class="front-cover">
      <div class="front-scene" role="img" aria-label="Bright cloudy sky above green alpine mountains with a meadow of yellow wildflowers in the foreground"></div>
      <p class="author">MIRA HALDEN-SOREL</p>
      <h1>
        <span class="title-lead gold">Lanterns Over</span>
        <span class="title-main gold">Saltmere</span>
      </h1>
      <div class="subtitle-band">
        <p class="subtitle">Über den tod und das leben danach</p>
      </div>
      <p class="publisher">Cedarhall Press</p>
    </section>
  </main>
</body>
</html>
```